Digital & Print Graphic Design templates for Comedy Club

We need new new digital & print graphic design templates for our upcoming comedy events created for use in CANVA in the following specs
Digital:
1080x1080px
1200x600px
800x400px
1920x1080px
1080x1355px
1500x500px
851x315px
Print
11x17"
22x28"
95.5x30"

Target Market(s)

18+ comedy fans

Industry/Entity Type

comedy club

Font styles to use
Sans Serif

Colors
FFF300
FFF600
FEFA6F
FFFEC7
FFFEE8
6B429C
8869AF
B7A5CE
E3DAEB
F3F0F8

Requirements
Must have
• templates must be CANVA compatible. frame for comedian photo.
Nice to have
• would like to incorporate deep purple into the design
Should not have
• do not include phone number on any templates

```html
<!DOCTYPE html>
<html lang="en">
<head>
<meta charset="utf-8">
<title>Jon Kalbe – Live at Giggle Vault</title>
<link rel="stylesheet" href="https://fonts.googleapis.com/css2?family=Montserrat:wght@600;700;800;900&display=swap">
<style>
  :root {
    --yellow: #FFF300;
    --yellow-soft: #FEFA6F;
    --cream: #FFFEC7;
    --purple-deep: #2a0f5e;
    --purple: #6B429C;
    --purple-mid: #8869AF;
    --lavender: #B7A5CE;
    --lavender-pale: #E3DAEB;
    --white: #FFFFFF;
    --ink: #111111;
    --shadow-olive: #5a5300;
  }
  * { margin: 0; padding: 0; box-sizing: border-box; }
  html, body { width: 1200px; height: 1200px; overflow: hidden; background: var(--purple-deep); }
  .poster {
    position: relative;
    width: 1200px; height: 1200px;
    overflow: hidden;
    font-family: "Montserrat", sans-serif;
    color: var(--white);
    background:
      radial-gradient(circle at 136px 228px, rgba(255,240,200,.55) 0, rgba(255,200,120,.15) 40px, transparent 110px),
      radial-gradient(circle at 1102px 410px, rgba(255,240,200,.55) 0, rgba(255,200,120,.15) 40px, transparent 110px),
      radial-gradient(ellipse at 50% 45%, #5b2fb0 0%, #3b1686 45%, #230b55 100%);
  }
  .wall { position: absolute; inset: 0; }
  .headline {
    position: absolute; top: 72px; left: 0; right: 0;
    text-align: center;
    font-weight: 700; font-size: 36px; letter-spacing: 1px;
  }
  .ring { position: absolute; left: 0; top: 0; }
  .comedian-photo {
    position: absolute;
    left: 336px; top: 140px; width: 550px; height: 680px;
    border-radius: 240px 240px 0 0;
    background: linear-gradient(180deg, #b07f62 0%, #c99a7e 35%, #7a5a48 62%, #1c1c1f 78%, #151518 100%);
  }
  .club-badge {
    position: absolute;
    left: 75px; top: 528px; width: 216px; height: 216px;
    border-radius: 50%;
    background: var(--ink);
    border: 4px solid var(--white);
    display: flex; align-items: center; justify-content: center;
    text-align: center;
    font-weight: 900; font-size: 30px; line-height: 1.05;
    color: var(--yellow);
  }
  .comedian-name {
    position: absolute; left: 0; right: 0; top: 770px;
    text-align: center;
    white-space: nowrap;
    line-height: 1;
    font-weight: 900; font-size: 162px; letter-spacing: 4px;
    color: var(--yellow);
    transform: scaleY(1.3);
    transform-origin: top center;
    text-shadow: 2px 2px 0 var(--shadow-olive), 4px 4px 0 var(--shadow-olive), 6px 6px 0 var(--shadow-olive), 8px 8px 0 var(--shadow-olive);
  }
  .event-details {
    position: absolute; top: 1022px; left: 0; right: 0;
    display: flex; justify-content: center; gap: 62px;
    font-weight: 700; font-size: 27px;
  }
  .detail { display: flex; align-items: center; gap: 18px; }
  .detail svg { width: 52px; height: 52px; }
  .venue-line {
    position: absolute; top: 1104px; left: 0; right: 0;
    display: flex; justify-content: center; align-items: center; gap: 24px;
    font-weight: 700; font-size: 24px;
  }
  .dot { width: 11px; height: 11px; border-radius: 50%; background: var(--white); }
</style>
</head>
<body>
<main class="poster">
  <div class="wall" role="img" aria-label="Purple brick wall backdrop with stage light flares"></div>

  <h2 class="headline">LIVE AT GIGGLE VAULT</h2>

  <svg class="ring" width="1200" height="1200" viewBox="0 0 1200 1200" aria-hidden="true">
    <defs>
      <filter id="glow" x="-20%" y="-20%" width="140%" height="140%">
        <feGaussianBlur stdDeviation="6" result="b"/>
        <feMerge><feMergeNode in="b"/><feMergeNode in="SourceGraphic"/></feMerge>
      </filter>
    </defs>
    <circle cx="609" cy="588" r="378" fill="none" stroke="#FEFA6F" stroke-width="6" filter="url(#glow)"/>
    <circle cx="609" cy="588" r="352" fill="none" stroke="#B7A5CE" stroke-width="44"/>
    <circle cx="609" cy="588" r="326" fill="none" stroke="#FFFEC7" stroke-width="6" filter="url(#glow)"/>
    <g fill="#FFFEC7" filter="url(#glow)">
      <circle cx="961" cy="588" r="12"/><circle cx="945" cy="697" r="12"/><circle cx="898" cy="795" r="12"/>
      <circle cx="824" cy="874" r="12"/><circle cx="394" cy="874" r="12"/><circle cx="320" cy="795" r="12"/>
      <circle cx="273" cy="697" r="12"/><circle cx="257" cy="588" r="12"/><circle cx="273" cy="479" r="12"/>
      <circle cx="320" cy="381" r="12"/><circle cx="394" cy="302" r="12"/><circle cx="824" cy="302" r="12"/>
      <circle cx="898" cy="381" r="12"/><circle cx="945" cy="479" r="12"/>
    </g>
  </svg>

  <div class="comedian-photo" role="img" aria-label="Comedian headshot photo"></div>

  <div class="club-badge">THE GIGGLE<br>VAULT</div>

  <h1 class="comedian-name">JON KALBE</h1>

  <div class="event-details">
    <div class="detail">
      <svg viewBox="0 0 52 52" aria-hidden="true">
        <rect x="2" y="2" width="48" height="48" rx="6" fill="#FFF300"/>
        <rect x="10" y="12" width="32" height="30" rx="2" fill="none" stroke="#111" stroke-width="3"/>
        <line x1="10" y1="19" x2="42" y2="19" stroke="#111" stroke-width="3"/>
        <line x1="17" y1="8" x2="17" y2="15" stroke="#111" stroke-width="3"/>
        <line x1="35" y1="8" x2="35" y2="15" stroke="#111" stroke-width="3"/>
        <g fill="#111"><rect x="15" y="24" width="4" height="4"/><rect x="24" y="24" width="4" height="4"/><rect x="33" y="24" width="4" height="4"/><rect x="15" y="32" width="4" height="4"/><rect x="24" y="32" width="4" height="4"/><rect x="33" y="32" width="4" height="4"/></g>
      </svg>
      <span>Wednesday 4 Feb, 2026</span>
    </div>
    <div class="detail">
      <svg viewBox="0 0 52 52" aria-hidden="true">
        <rect x="2" y="2" width="48" height="48" rx="6" fill="#FFF300"/>
        <circle cx="26" cy="26" r="15" fill="none" stroke="#111" stroke-width="3"/>
        <polyline points="26,17 26,26 33,30" fill="none" stroke="#111" stroke-width="3" stroke-linecap="round"/>
      </svg>
      <span>7:00pm - 10:00pm</span>
    </div>
  </div>

  <div class="venue-line">
    <span>At The Giggle Vault</span><span class="dot"></span>
    <span>123 Anywhere St., Any City</span><span class="dot"></span>
    <span>Free Parking Area</span>
  </div>
</main>
</body>
</html>
```